Wellness Coach needs a Business Card

I need a business card for a start-up coaching business called Brightfern Vitality Partners. I don't have a logo as such but I am looking to have a web page created in a few months time and hopefully the person who designs this card will be able to do or help with the web project. This business card will be used primarily for networking and for initial clients.

As the name implies, the coaching focus is wide-ranging and includes multiple facets of health and wellness, including physical, mental, spiritual, etc. I am a Personal Trainer so the main focus will be physical training, but with the other areas of life / wellness included.

My information for the card:

Rowan Tesdale
Director
Brightfern Vitality Partners

Phone: 0413 862051
Address: PO Box 615 Mitchell ACT 2911
email: rowan@brightfernvitalitypartners.com.au
web: http://www.brightfernvitalitypartners.com.au

Target Market(s)

People wanting to change their life by getting fit and by addressing issues in their lives that are holding them back. I will target people already into fitness but who want to extend their approach into life coaching.

Industry/Entity Type

Health

Requirements
Must have
• - I am keen on a single sided business card design but if your design lends itself to a double sided design then I'm open to that thanks.

- I love the idea of fresh - something that represents the awakening of somebody who has been dormant. Lime green strikes me as fresh, but this is just an idea, not mandatory.
Nice to have
• - I'm keen for minimisation but I don't mind an image in the background taking up the whole space, as long as it is not too busy.

- Two types of images that I can visualise are a mountain summit or a path leading into nature or up a mountain - an adventure! Again, not mandatory, just an idea.
Should not have
• - I'm not keen on over-crowding.
- One image I'm not keen on is someone standing on top of a mountain with their arms in the air - too cliché.

```html
<!DOCTYPE html>
<html lang="en">
<head>
<meta charset="UTF-8">
<title>Brightfern Vitality Partners – Business Card</title>
<link rel="stylesheet" href="https://fonts.googleapis.com/css2?family=Didact+Gothic&display=swap">
<style>
  :root {
    --lime: #68c41c;
    --lime-light: #84d93c;
    --lime-deep: #4c9a16;
    --lime-shadow: #5aae1a;
    --ink: #ffffff;
  }
  html, body {
    margin: 0;
    padding: 0;
    overflow: hidden;
    background: #ffffff;
  }
  .card {
    position: relative;
    width: 1200px;
    height: 702px;
    overflow: hidden;
    background: var(--lime);
    font-family: "Didact Gothic", "Century Gothic", sans-serif;
    color: var(--ink);
  }
  .card__backdrop {
    position: absolute;
    inset: 0;
    background:
      radial-gradient(ellipse 50% 40% at 48% 60%, var(--lime-light) 0%, rgba(132,217,60,0) 70%),
      radial-gradient(ellipse 35% 30% at 72% 52%, var(--lime-shadow) 0%, rgba(90,174,26,0) 70%),
      radial-gradient(ellipse 30% 25% at 22% 70%, var(--lime-shadow) 0%, rgba(90,174,26,0) 70%),
      linear-gradient(180deg, var(--lime) 0%, var(--lime) 30%, var(--lime-light) 58%, var(--lime-deep) 100%);
  }
  .card__line {
    position: absolute;
    left: 0;
    width: 100%;
    margin: 0;
    text-align: center;
    line-height: 1;
    font-weight: 400;
    white-space: nowrap;
  }
  .card__name    { top: 90px;  font-size: 68px; }
  .card__role    { top: 172px; font-size: 31px; }
  .card__company { top: 242px; font-size: 71px; }
  .card__contact { font-size: 37px; }
  .card__contact--phone   { top: 389px; }
  .card__contact--address { top: 452px; }
  .card__contact--email   { top: 513px; }
  .card__contact--web     { top: 571px; }
</style>
</head>
<body>
  <div class="card">
    <div class="card__backdrop" role="img" aria-label="Watercolour mountain summit rising through the centre, rendered in lime green tones"></div>
    <h1 class="card__line card__name">Rowan Tesdale</h1>
    <p class="card__line card__role">Director</p>
    <p class="card__line card__company">Brightfern Vitality Partners</p>
    <p class="card__line card__contact card__contact--phone">Phone: 0413 862051</p>
    <p class="card__line card__contact card__contact--address">Address: PO Box 615 Kestrel Vale ACT 2908</p>
    <p class="card__line card__contact card__contact--email">email: rowan@brightfernvitalitypartners.com.au</p>
    <p class="card__line card__contact card__contact--web">web: http://www.brightfernvitalitypartners.com.au</p>
  </div>
</body>
</html>
```